Business Card Design Project for Electrical Company

We need a business card designed for a new Electrical Company called Dorvel Electrical Solutions, i dont mind if only Dorvel Electrical is used. We are a domestic and commercial Electrical Company that provides a range of Electrical Services. Our Company colours are Fluro Yellow and Black with the Lightning bolt picture attached.I have attached a card that has been made i think it is rather basic and am looking for something more. the font of Dorvel Electrical has been used on our car graphics as well as the lightning bolt. i want to keep them the same so we can brand our business. Some things we want on the front of the card are Dorvel Electrical Solutions, Owen Platt, 0438516274, admin@dorvelelectrical.example, Lic No 58342, Servicing CQ Region. But we want Owens name seperate to the phone number as its the phone number for the office, owen wont be answering the phone so we are thinking we dont want to give that impression. What do you think? with all that if you have complete different font designs please submit what you think would work best. keeping in mind our company name and details as well as coulors.

Industry/Entity Type

Business

```html
<!DOCTYPE html>
<html lang="en">
<head>
<meta charset="utf-8">
<title>Dorvel Electrical Solutions – Business Card</title>
<link rel="stylesheet" href="https://fonts.googleapis.com/css2?family=Montserrat:wght@300;400;700;800&display=swap">
<style>
  :root {
    --fluro: #c9d92a;
    --charcoal: #2b2b2b;
    --charcoal-deep: #242424;
    --paper: #f7f7f5;
    --ink-light: #e6e6e6;
    --ink-muted: #bdbdbd;
    --backdrop: #e4e4e1;
  }
  * { box-sizing: border-box; margin: 0; padding: 0; }
  html, body {
    width: 1200px;
    height: 800px;
    overflow: hidden;
  }
  body {
    background: var(--backdrop);
    font-family: "Montserrat", sans-serif;
    display: flex;
    align-items: center;
    justify-content: center;
    gap: 40px;
  }
  .card {
    position: relative;
    width: 540px;
    height: 330px;
    overflow: hidden;
    box-shadow: 0 10px 30px rgba(0,0,0,.18);
  }

  /* ---------- Front ---------- */
  .card--front { background: var(--charcoal); }
  .front__top {
    position: absolute;
    inset: 0 0 auto 0;
    height: 196px;
    background: var(--paper);
  }
  .bolt-art { position: absolute; }
  .front__top .bolt-art {
    right: 60px;
    top: 0;
    width: 280px;
    height: 196px;
    background: radial-gradient(closest-side at 55% 45%, #d6d6d3 0%, #e9e9e7 50%, rgba(247,247,245,0) 100%);
  }
  .wordmark {
    position: absolute;
    font-weight: 800;
    text-transform: uppercase;
    line-height: .95;
    letter-spacing: .5px;
  }
  .front__top .wordmark {
    right: 36px;
    top: 58px;
    color: var(--charcoal);
    font-size: 34px;
  }
  .wordmark span { display: block; }
  .accent-stripe {
    position: absolute;
    left: 0; right: 0;
    height: 9px;
    background: var(--fluro);
  }
  .card--front .accent-stripe { top: 196px; }
  .front__bottom {
    position: absolute;
    inset: 205px 0 0 0;
    display: flex;
    justify-content: space-between;
    align-items: flex-end;
    padding: 0 30px 28px 36px;
  }
  .person__name {
    color: var(--ink-light);
    font-weight: 700;
    font-size: 17px;
    letter-spacing: .5px;
    text-transform: uppercase;
  }
  .person__role {
    color: var(--ink-muted);
    font-weight: 300;
    font-size: 15px;
    margin-top: 4px;
  }
  .contact {
    list-style: none;
    align-self: flex-start;
    margin-top: 18px;
    width: 250px;
  }
  .contact li {
    display: flex;
    align-items: center;
    gap: 10px;
    color: var(--ink-light);
    font-weight: 300;
    font-size: 12.5px;
    line-height: 16px;
    margin-bottom: 7px;
  }
  .contact svg { width: 16px; height: 16px; flex: none; }

  /* ---------- Back ---------- */
  .card--back { background: var(--charcoal-deep); }
  .card--back .bolt-art {
    left: 280px;
    top: 0;
    width: 240px;
    height: 180px;
    background: radial-gradient(closest-side at 45% 40%, #474747 0%, #333 50%, rgba(36,36,36,0) 100%);
  }
  .card--back .wordmark {
    left: 290px;
    top: 48px;
    color: var(--fluro);
    font-size: 30px;
  }
  .services {
    position: absolute;
    list-style: none;
    color: var(--ink-light);
    font-weight: 400;
    font-size: 14px;
  }
  .services li {
    position: relative;
    padding-left: 16px;
    margin-bottom: 9px;
  }
  .services li::before {
    content: "";
    position: absolute;
    left: 0; top: 7px;
    width: 5px; height: 5px;
    border-radius: 50%;
    background: var(--ink-light);
  }
  .services--main { left: 36px; top: 58px; }
  .services--extra { left: 298px; top: 178px; }
  .card--back .accent-stripe { bottom: 26px; }
</style>
</head>
<body>

  <section class="card card--front" aria-label="Business card front">
    <div class="front__top">
      <div class="bolt-art" role="img" aria-label="Lightning bolt illustration"></div>
      <div class="wordmark"><span>Dorvel</span><span>Electrical</span><span>Solutions</span></div>
    </div>
    <div class="accent-stripe"></div>
    <div class="front__bottom">
      <div class="person">
        <p class="person__name">Owen Platt</p>
        <p class="person__role">Licensed Electrician</p>
      </div>
      <ul class="contact">
        <li>
          <svg viewBox="0 0 16 16" aria-hidden="true"><rect x="4" y="1" width="8" height="14" rx="1.5" fill="none" stroke="var(--fluro)" stroke-width="1.6"/><rect x="5.8" y="3" width="4.4" height="8" fill="var(--fluro)"/><circle cx="8" cy="13" r=".9" fill="var(--fluro)"/></svg>
          0438 516 274
        </li>
        <li>
          <svg viewBox="0 0 16 16" aria-hidden="true"><rect x="1" y="3.5" width="14" height="9" fill="var(--fluro)"/><path d="M1 3.5 L8 9 L15 3.5" fill="none" stroke="var(--charcoal)" stroke-width="1.2"/></svg>
          admin@dorvelelectrical.example
        </li>
        <li>
          <svg viewBox="0 0 16 16" aria-hidden="true"><rect x="1.5" y="3" width="13" height="10" rx="1.2" fill="none" stroke="var(--fluro)" stroke-width="1.6"/><rect x="4" y="6" width="4" height="4" fill="var(--fluro)"/></svg>
          Lic No 58342
        </li>
        <li>
          <svg viewBox="0 0 16 16" aria-hidden="true"><path d="M8 15 C8 15 3 9.5 3 6 A5 5 0 0 1 13 6 C13 9.5 8 15 8 15 Z" fill="var(--fluro)"/><circle cx="8" cy="6" r="1.8" fill="var(--charcoal)"/></svg>
          Servicing CQ Region
        </li>
      </ul>
    </div>
  </section>

  <section class="card card--back" aria-label="Business card back">
    <div class="bolt-art" role="img" aria-label="Lightning bolt illustration"></div>
    <div class="wordmark"><span>Dorvel</span><span>Electrical</span><span>Solutions</span></div>
    <ul class="services services--main">
      <li>Light &amp; Power</li>
      <li>TV &amp; Data</li>
      <li>Test &amp; Tagging</li>
      <li>Residential</li>
      <li>Renovations</li>
      <li>Design &amp; Installation</li>
    </ul>
    <ul class="services services--extra">
      <li>Air Con Installation</li>
      <li>Smoke Detectors</li>
    </ul>
    <div class="accent-stripe"></div>
  </section>

</body>
</html>
```